Web Design Project

We are a SaaS company that specializes in the thrift industry POS and inventory software. We want a clean and professional site that does NOT look like a template site.

*** A little more about our business -
We offer a SaaS (Software As A Service) for a Point Of Sale and inventory control product specifically for the Thrift / Second hand industry. The software allows them to process inventory, grade/rate it, create the barcoded tags. It the does the whole retail sale process. We also offer tie-ins to Pixelyard, Chirpnest and apple/droid mobile apps to support our customers thrift stores.

We need to in incorporate the look/feel and color scheme of our logo.

I would imagine possibly a HTML5 slideshow (3-5 slides) rotating on the home page showing screenshots, etc.

I am envisioning icons representing features of our product.

PLEASE ask questions, I am sure I have left out a ton.
Updates

Requirements
Must have
• I have attached a couple of our logo's with color options. It needs to flow with that.

I have also attached a screen shot of what I think might work. This DOESN'T suggest that is what I am looking for, just a sample.

I am thinking a home page and maybe one or two sub pages
***Update, I kind of like the following concept for one of the sub-pages
http://www.quotivex.example/estimate.html

There should also be a place to highlight Pixelyard and chirpnest.

It will be a bilingual / multilingual site, so take that into account
Should not have
• I don't want it to look like a template site. It should be clean and professional.

```html
<!DOCTYPE html>
<html lang="en">
<head>
<meta charset="utf-8">
<title>resalewise — Welcome</title>
<link rel="stylesheet" href="https://fonts.googleapis.com/css2?family=Source+Sans+3:wght@400;600;700&display=swap">
<style>
:root{
  --bar-dark:#333435;
  --bar-top:#8d9499;
  --hero-light:#f3f6f8;
  --hero-mid:#dde4ea;
  --ink:#34474f;
  --muted:#7b94a6;
  --title:#5f7384;
  --body:#595f63;
  --dash:#b6bec4;
  --blue:#2d9fdc;
  --blue-light:#7ccbf1;
  --blue-dark:#1f85bf;
  --footer:#3b3c3d;
  --footer-text:#c8c9ca;
  --footer-line:#555;
  --base:#bfc7cb;
  --white:#ffffff;
}
*{margin:0;padding:0;box-sizing:border-box}
html,body{width:1200px;height:918px;overflow:hidden}
body{position:relative;font-family:"Source Sans 3",Arial,sans-serif;background:var(--hero-mid)}

/* header */
.site-header{position:absolute;left:0;top:0;width:1200px;height:84px;background:var(--bar-dark);border-top:4px solid var(--bar-top);border-bottom:1px solid #555}
.brand{position:absolute;left:108px;top:15px;display:flex;align-items:center;gap:10px}
.brand-mark{width:36px;height:36px;background:var(--blue);border-radius:4px}
.brand-name{font-size:30px;font-weight:700;color:var(--blue);letter-spacing:-.5px}
.main-nav a{position:absolute;top:24px;font-size:16px;font-weight:600;color:var(--white);text-decoration:none;line-height:28px}
.main-nav a.current{left:560px;width:62px;text-align:center;color:#3a4348;background:linear-gradient(#fafafa,#cfd4d7);border-radius:4px;box-shadow:0 2px 2px rgba(0,0,0,.5)}

/* hero */
.hero{position:absolute;left:0;top:84px;width:1200px;height:337px;background:radial-gradient(ellipse at 50% 10%,var(--hero-light),#e2e8ec 60%,#d3dbe1);border-bottom:1px solid #c3ccd2}
.hero h1{position:absolute;left:170px;top:34px;font-size:35px;font-weight:400;color:var(--ink);letter-spacing:-.3px}
.hero h1 strong{font-weight:700}
.dash{position:absolute;height:0;border-top:1px dashed var(--dash)}
.hero p{position:absolute;left:170px;top:104px;width:436px;font-size:17px;line-height:27.5px;color:var(--muted);letter-spacing:-.2px}
.hero p .line{display:block;white-space:nowrap;text-align:justify;text-align-last:justify}
.hero p .line.last{text-align-last:left}
.hero p a{color:var(--title);font-weight:700;text-decoration:underline}
.btn-read{position:absolute;left:300px;top:263px;width:144px;height:42px;border-radius:5px;background:linear-gradient(var(--blue-light),var(--blue) 55%,var(--blue-dark));color:var(--white);font-size:17px;font-weight:700;text-align:center;line-height:42px;box-shadow:0 6px 8px -4px rgba(0,0,0,.35);text-shadow:0 1px 1px rgba(0,0,0,.3)}
.arrow{position:absolute;top:150px;width:32px;height:32px}
.shot-back{position:absolute;left:703px;top:51px;width:343px;height:210px;background:linear-gradient(#cfe7f3,#2b9fd6);border-radius:6px;border:3px solid #e5e9ec}
.shot-front{position:absolute;left:648px;top:60px;width:375px;height:232px;background:linear-gradient(#fdfdfd,#e8edf0 40%,#d5dde2);border-radius:6px;border:3px solid #eef1f3;box-shadow:0 12px 14px -8px rgba(0,0,0,.35)}
.dots{position:absolute;z-index:5;left:557px;top:420px;width:92px;height:25px;background:linear-gradient(#3a3b3c,#1c1d1e);border-radius:0 0 4px 4px;display:flex;justify-content:center;align-items:center;gap:5px}
.dots span{width:6px;height:6px;border-radius:50%;background:#6a6d70}
.dots span.on{width:9px;height:9px;background:var(--blue)}

/* features */
.features{position:absolute;left:0;top:421px;width:1200px;height:271px;background:linear-gradient(#d6dde2,#e6ebee 40%,#dfe5e9)}
.feature{position:absolute;top:47px;width:232px}
.feature .icon{position:absolute;left:0;top:0;width:42px;height:38px}
.feature h2{position:absolute;top:1px;font-size:19px;font-weight:600;color:var(--title);white-space:nowrap;line-height:22px;letter-spacing:-.2px}
.feature .sub{position:absolute;top:21px;font-size:12px;color:#8a9aa6}
.feature .text{position:absolute;left:0;top:62px;width:232px;font-size:12px;line-height:18px;color:var(--body);text-align:justify;letter-spacing:-.25px}
.btn-more{position:absolute;top:215px;width:80px;height:22px;border-radius:3px;background:linear-gradient(var(--blue-light),var(--blue) 60%,var(--blue-dark));color:var(--white);font-size:11px;font-weight:700;text-align:center;line-height:22px}

/* footer */
.site-footer{position:absolute;left:0;top:692px;width:1200px;height:184px;background:radial-gradient(ellipse at 40% 40%,#454647,var(--footer))}
.site-footer h3{position:absolute;top:18px;font-size:13px;font-weight:700;color:var(--white)}
.sitemap{position:absolute;left:108px;top:44px;width:138px;list-style:none}
.sitemap li{height:24px;border-bottom:1px solid var(--footer-line);font-size:12px;line-height:20px;color:var(--footer-text);padding-left:11px;position:relative}
.sitemap li::before{content:"›";position:absolute;left:0;top:0;color:#e07b3a}
.footer-about{position:absolute;left:308px;top:50px;width:320px;font-size:12px;line-height:16px;color:var(--footer-text)}
.map{position:absolute;left:673px;top:52px;width:109px;height:109px;border-radius:6px;border:2px solid #9a9c9e;background:linear-gradient(135deg,#ecebe3,#d9dccf)}
.foot-brand{position:absolute;left:816px;top:64px;display:flex;align-items:center;gap:5px}
.foot-brand i{width:13px;height:13px;background:var(--blue);display:block}
.foot-brand span{font-size:14px;font-weight:700;color:var(--blue)}
.address{position:absolute;left:816px;top:98px;font-size:12px;line-height:16px;color:var(--white);font-weight:600}
.contact{position:absolute;left:952px;top:65px;font-size:12px;line-height:16px;color:var(--white);font-weight:600}
.contact a{color:var(--blue);text-decoration:underline}
.contact .web{color:var(--blue)}
.base-bar{position:absolute;left:0;top:876px;width:1200px;height:42px;background:linear-gradient(#c6cdd1,#b7bfc4);border-top:1px solid #d6dcdf;font-size:10px;color:#3e4448}
.base-bar .copy{position:absolute;left:110px;top:13px}
.base-bar .links{position:absolute;right:100px;top:13px}
</style>
</head>
<body>

<header class="site-header">
  <div class="brand"><span class="brand-mark"></span><span class="brand-name">resalewise</span></div>
  <nav class="main-nav">
    <a class="current" href="#">Home</a>
    <a href="#" style="left:666px">About Us</a>
    <a href="#" style="left:783px">Our Offer</a>
    <a href="#" style="left:903px">Gallery</a>
    <a href="#" style="left:1005px">Contact Us</a>
  </nav>
</header>

<section class="hero">
  <h1><strong>Wellcome</strong> to our website !</h1>
  <div class="dash" style="left:170px;top:91px;width:436px"></div>
  <p>
    <span class="line">Vestibulum dapibus, mauris nec malesuada fames ac turpis</span>
    <span class="line">velit, rhoncus eu, luctus et interdum adipiscing wisi.&nbsp; Aliquam</span>
    <span class="line">erat ac ipsum. <a href="#">Integer aliquam purus</a>. Quisque lorem tortor</span>
    <span class="line last">fringilla sed, vestibulum id.</span>
  </p>
  <div class="dash" style="left:170px;top:236px;width:436px"></div>
  <div class="btn-read">READ MORE</div>

  <svg class="arrow" style="left:108px" viewBox="0 0 32 32"><circle cx="16" cy="16" r="16" fill="#8a959c"/><path d="M19 8l-8 8 8 8" fill="none" stroke="#fff" stroke-width="4"/></svg>
  <svg class="arrow" style="left:1067px" viewBox="0 0 32 32"><circle cx="16" cy="16" r="16" fill="#c7ced2"/><path d="M13 8l8 8-8 8" fill="none" stroke="#fff" stroke-width="4"/></svg>

  <div class="shot-back" role="img" aria-label="Second software screenshot behind the first"></div>
  <div class="shot-front" role="img" aria-label="Screenshot of the web application dashboard with user panels"></div>
</section>

<div class="dots"><span></span><span></span><span class="on"></span><span></span><span></span></div>

<section class="features">
  <div class="dash" style="left:108px;top:96px;width:992px"></div>
  <div class="dash" style="left:108px;top:215px;width:992px"></div>

  <article class="feature" style="left:108px">
    <svg class="icon" viewBox="0 0 42 38"><rect x="14" y="3" width="14" height="7" rx="2" fill="none" stroke="#5a2e14" stroke-width="3"/><rect x="2" y="9" width="38" height="27" rx="4" fill="#9a4a1c"/><rect x="2" y="19" width="38" height="2" fill="#6b3010"/></svg>
    <h2 style="left:53px">Why our company</h2><div class="sub" style="left:53px">Lorem ipsum dolor</div>
    <div class="text">Aliquam erat ac ipsum. Integer aliquam purus. Quisque lorem tortor fringilla sed, vestibulum id, eleifend justo vel bibendum sapien massa ac turpis faucibus orci luctus non, consectetuer lobortis quis, varius in, purus.</div>
  </article>
  <div class="btn-more" style="left:184px">MORE</div>

  <article class="feature" style="left:361px">
    <svg class="icon" viewBox="0 0 42 38"><circle cx="18" cy="19" r="17" fill="#2a8fd6" stroke="#d6dde2" stroke-width="2"/><circle cx="19" cy="11" r="2.6" fill="#fff"/><path d="M16 17h5l-2 12h-4" fill="#fff"/></svg>
    <h2 style="left:45px">About our products</h2><div class="sub" style="left:45px">Lorem ipsum dolor</div>
    <div class="text">Aliquam erat ac ipsum. Integer aliquam purus. Quisque lorem tortor fringilla sed, vestibulum id, eleifend justo vel bibendum sapien massa.<br><br>Nullam viverra consectetuer.</div>
  </article>
  <div class="btn-more" style="left:441px">MORE</div>

  <article class="feature" style="left:614px">
    <svg class="icon" viewBox="0 0 42 38"><path d="M3 6h16l12 12-13 13L3 18z" fill="#e0892a"/><circle cx="9" cy="12" r="2.5" fill="#fff"/></svg>
    <h2 style="left:38px">Our offer</h2><div class="sub" style="left:38px">Lorem ipsum dolor</div>
    <div class="text">Aliquam erat ac ipsum. Integer aliquam purus. Quisque lorem tortor fringilla sed, vestibulum id, eleifend justo vel bibendum. Integer ultrices posuere cubilia Curae, Nulla ipsum dolor lacus, suscipit adipiscing.</div>
  </article>
  <div class="btn-more" style="left:699px">MORE</div>

  <article class="feature" style="left:868px">
    <svg class="icon" viewBox="0 0 42 38"><circle cx="18" cy="19" r="17" fill="#1f7fd2"/><ellipse cx="18" cy="19" rx="8" ry="17" fill="none" stroke="#9fd3f5" stroke-width="1.5"/><path d="M1 19h34M4 10h28M4 28h28" stroke="#9fd3f5" stroke-width="1.5"/></svg>
    <h2 style="left:45px">We on Web</h2><div class="sub" style="left:45px">Lorem ipsum dolor</div>
    <div class="text">Integer ultrices posuere cubilia Curae, Nulla ipsum dolor lacus, suscipit adipiscing. Cum sociis natoque penatibus et ultrices volutpat. Nullam wisi ultricies a, gravida vitae, dapibus risus</div>
  </article>
  <div class="btn-more" style="left:946px">MORE</div>
</section>

<footer class="site-footer">
  <h3 style="left:108px">SITEMAP</h3>
  <ul class="sitemap">
    <li>Home</li><li>About us</li><li>Our offer</li><li>Gallery</li><li>Contact Us</li>
  </ul>

  <h3 style="left:308px">LOREM IPSUM DOLOR</h3>
  <p class="footer-about">Nullam viverra consectetuer. Quisque cursus et, porttitor risus. Aliquam sem. In hendrerit nulla quam nunc, accumsan congue. Lorem ipsum primis in nibh vel risus. Sed vel lectus. Ut sagittis, ipsum dolor quam.</p>

  <h3 style="left:672px">CONTACT DETAILS</h3>
  <div class="map" role="img" aria-label="Street map showing the office location"></div>
  <div class="foot-brand"><i></i><span>resalewise</span></div>
  <div class="address">Owen Hartley<br>Linden Row 4/7<br>051178 Marrow Bay</div>
  <div class="contact">tel. +00 000 000 000<br>fax. +00 000 000 000<br><br>e-mail: <a href="#">info@sitename.example</a><br><span class="web">www.sitename.example</span></div>
</footer>

<div class="base-bar">
  <span class="copy">Copyright by Sitename.example</span>
  <span class="links">Add to bookmarks &nbsp;|&nbsp; Privacy Policy &nbsp;|&nbsp; XML Sitemap</span>
</div>

</body>
</html>
```